Small Business Consulting Firm Needs Business Card Design

Need a sleek modern business card with 2 sides matching the colors of our logo. We will be placing these with a mailer we are sending out. These business cards will only ever be given to business owners. We operate helping businesses who are struggling with cash flow or finances. If the green and blue design needs to be moved to the right of "Brightpath Ledger Consulting" for aesthetic purposes that is ok. We will need an editable file if possible. We would like to include the reps name, email, website, and phone number. For now just use Owen Parrish, oparrish@brightpathledger.com, www.brightpathledger.com, and 855-219-7038.

```html
<!DOCTYPE html>
<html lang="en">
<head>
<meta charset="utf-8">
<title>Brightpath Ledger Consulting – Business Card</title>
<link rel="stylesheet" href="https://fonts.googleapis.com/css2?family=Montserrat:wght@400&family=Open+Sans:wght@400;600&display=swap">
<style>
  :root {
    --bg: #e9e6e2;
    --card-front: #ffffff;
    --card-back: #2a2c2d;
    --emboss: #202223;
    --ink: #3a3a3a;
    --ink-soft: #444444;
    --green: #6cb33f;
    --blue: #1f7fc4;
  }
  * { margin: 0; padding: 0; box-sizing: border-box; }
  html, body { width: 1200px; height: 1000px; overflow: hidden; }
  body {
    background: var(--bg);
    position: relative;
    font-family: "Open Sans", Arial, sans-serif;
  }
  .card {
    position: absolute;
    left: 266px;
    width: 666px;
    height: 397px;
    box-shadow: 0 4px 14px rgba(0,0,0,0.18);
  }
  .card--front { top: 74px; background: var(--card-front); }
  .card--back { top: 533px; background: var(--card-back); }

  .brand {
    position: absolute;
    text-align: center;
    font-family: "Montserrat", Arial, sans-serif;
    font-weight: 400;
  }
  .card--front .brand { left: 20px; width: 340px; top: 125px; color: var(--ink); }
  .brand__mark { display: block; margin: 0 auto; }
  .card--front .brand__mark { width: 56px; height: 56px; background: var(--green); margin-bottom: 18px; }
  .brand__name { display: block; font-size: 24px; letter-spacing: 1px; white-space: nowrap; }
  .brand__sub { display: block; font-size: 13px; letter-spacing: 5px; margin-top: 4px; }

  .contact { position: absolute; left: 372px; top: 94px; color: var(--ink-soft); }
  .contact__name { color: var(--green); font-weight: 600; font-size: 21px; line-height: 26px; }
  .contact__title { font-size: 16px; line-height: 22px; }
  .contact__rule { width: 44px; height: 3px; background: var(--green); margin: 12px 0 14px; }
  .contact__address { font-size: 16.5px; line-height: 24px; margin-bottom: 10px; }
  .contact__line { display: flex; align-items: center; font-size: 17px; line-height: 24.5px; }
  .contact__icon { width: 14px; height: 14px; margin-right: 8px; flex: none; }

  .card--back .brand { left: 0; width: 666px; top: 92px; color: var(--emboss); }
  .card--back .brand__mark { width: 138px; height: 138px; background: var(--emboss); margin-bottom: 38px; }
  .card--back .brand__name { font-size: 34px; letter-spacing: 1.5px; }
  .card--back .brand__sub { font-size: 16px; letter-spacing: 8px; margin-top: 6px; }
</style>
</head>
<body>
  <section class="card card--front">
    <div class="brand">
      <span class="brand__mark"></span>
      <span class="brand__name">BRIGHTPATH LEDGER</span>
      <span class="brand__sub">CONSULTING</span>
    </div>
    <div class="contact">
      <p class="contact__name">DANIEL WHITCOMBE</p>
      <p class="contact__title">CEO / Owner</p>
      <div class="contact__rule"></div>
      <p class="contact__address">412 N. Market Street<br>Dayton, Ohio 45402</p>
      <p class="contact__line">
        <svg class="contact__icon" viewBox="0 0 14 14" aria-hidden="true"><path fill="#6cb33f" d="M1 5c0-2 2-3 6-3s6 1 6 3v1h-3V5H4v1H1zM3 7h8l1 5H2z"/><circle cx="7" cy="9.5" r="1.3" fill="#fff"/></svg>
        937-608-2751
      </p>
      <p class="contact__line">
        <svg class="contact__icon" viewBox="0 0 14 14" aria-hidden="true"><rect x="1" y="3" width="12" height="8" fill="#6cb33f"/><path d="M1 3l6 5 6-5" fill="none" stroke="#fff" stroke-width="1.2"/></svg>
        info@brightpathledger.com
      </p>
      <p class="contact__line">
        <svg class="contact__icon" viewBox="0 0 14 14" aria-hidden="true"><circle cx="7" cy="7" r="6" fill="#6cb33f"/><path d="M7 1v12M1 7h12" stroke="#fff" stroke-width="1"/></svg>
        www.brightpathledger.com
      </p>
    </div>
  </section>

  <section class="card card--back">
    <div class="brand">
      <span class="brand__mark"></span>
      <span class="brand__name">BRIGHTPATH LEDGER</span>
      <span class="brand__sub">CONSULTING</span>
    </div>
  </section>
</body>
</html>
```